Website Design - Photo Shop Design - Functional Cash Register Layout for POS System

Design a webpage for Point of Sale site. A cash register page.

Page must have a good look. I have attached a file of a possible layout example - but need a much nicer design. I have also attached the site logo. which i will upload without background tomorrow hopefully.

Looking for a nice Fresh look , not dark and dingy.

Target Market(s)

Business

Industry/Entity Type

Business Software

Number of Pages Required

1 page

Colors
f59195
f04a50
ec1f27
fbd4d5
ffffff
f8f3f8
fdf0f6
feeeee
ecf5f6

Requirements
Must have
• Cash register layout for POS software site. Nice layout ,
Nice to have
• Try putting he register part on the left side as well as the right - invert the designs have them different to the layout example shown too.
Should not have
• Not to dark

```html
<!DOCTYPE html>
<html lang="en">
<head>
<meta charset="utf-8">
<title>TillNest – Cash Register</title>
<link href="https://fonts.googleapis.com/css2?family=Montserrat:wght@400;500;600;700&display=swap" rel="stylesheet">
<style>
:root{
  --red:#ec1f27;
  --coral:#f04a50;
  --salmon:#f59195;
  --blush:#fbd4d5;
  --page:#fdf0f6;
  --tile:#f3eded;
  --white:#ffffff;
  --line:#ece6e8;
  --ink:#333333;
  --muted:#6a6a6a;
  --tile-ink:#c2b0b2;
}
*{box-sizing:border-box;margin:0;padding:0}
html,body{width:1200px;height:743px;overflow:hidden}
body{background:var(--page);font-family:"Montserrat",sans-serif;color:var(--ink);position:relative;font-size:11px}
.abs{position:absolute}

.topbar{left:0;top:0;width:1200px;height:27px}
.account-links{left:91px;top:7px;display:flex;gap:0;font-size:10.5px}
.account-links span{padding:0 10px;border-left:1px solid #bbb;line-height:12px}
.account-links span:first-child{padding-left:0;border-left:0}
.account-links b{font-weight:400;color:var(--red)}
.user{left:855px;top:5px;display:flex;align-items:center;gap:6px;font-size:11px}
.avatar{width:17px;height:17px;border-radius:50%;background:#d9c9c2}
.register-tag{left:976px;top:5px;width:135px;height:17px;background:var(--salmon);color:#fff;font-size:10.5px;text-align:center;line-height:17px}

.header{left:0;top:29px;width:1200px;height:64px;background:var(--white)}
.brand{left:91px;top:47px;display:flex;align-items:center;gap:8px;font-size:24px;font-weight:600;color:var(--red);letter-spacing:-.5px}
.brand-dot{width:20px;height:20px;border-radius:50%;background:var(--red)}
.nav-btn{top:48px;height:28px;background:var(--coral);color:#fff;font-size:11px;display:flex;align-items:center;gap:8px;padding:0 10px;border:1px solid #d93a40}
.nav-btn.active{background:var(--salmon);border-color:var(--salmon)}
.nav-ico{width:13px;height:11px;background:rgba(255,255,255,.75);border-radius:2px}
.badge{width:16px;height:16px;border-radius:50%;background:#fff;color:var(--coral);font-size:9.5px;font-weight:700;display:flex;align-items:center;justify-content:center}
.refresh{left:1077px;top:48px;width:32px;height:28px;background:var(--coral);display:flex;align-items:center;justify-content:center}

.panel{background:var(--white)}
.panel-head{height:33px;border-bottom:1px solid var(--line);display:flex;align-items:center;gap:8px;padding-left:16px;font-size:12px}
.products{left:91px;top:117px;width:742px;height:527px}
.mini-mark{width:16px;height:9px;border-radius:50%;background:var(--red)}
.tile{width:101px;height:89px;background:var(--tile)}
.tile .initials{display:block;text-align:center;font-size:38px;color:var(--tile-ink);padding-top:12px;letter-spacing:1px}
.tile .label{position:absolute;left:0;bottom:0;width:100%;height:19px;background:var(--salmon);color:#fff;font-size:10px;text-align:center;line-height:19px;white-space:nowrap;overflow:hidden}
.pager{top:604px;height:28px;background:#efe8e8;color:#777;font-size:10.5px;line-height:28px;text-align:center}

.categories{left:91px;top:661px;width:742px;height:30px;background:var(--coral);display:flex;color:#fff;font-size:11px}
.categories span{padding:0 12px;line-height:30px;border-right:1px solid #d73a40}
.categories .arrow{width:30px;padding:0;display:flex;align-items:center;justify-content:center}
.categories .fill{flex:1}
.categories .arrow.end{border-right:0;border-left:1px solid #d73a40}

.customer{left:857px;top:117px;width:252px;height:527px}
.customer .panel-head{justify-content:space-between;padding-right:14px}
.person{width:11px;height:13px}
.transaction{left:0;top:34px;width:252px;height:28px;background:#f1eded;font-size:10.5px;padding:0 13px;line-height:28px}
.transaction b{font-weight:400;color:var(--red)}
.add-notes{left:13px;top:346px;color:var(--red);font-size:10.5px;text-decoration:underline}
.totals{left:0;top:364px;width:252px}
.totals div{height:21.5px;background:#f1eded;border-bottom:1px solid #fff;display:flex;justify-content:space-between;padding:0 14px;font-size:10.5px;line-height:21px}
.totals em{font-style:normal;color:var(--red)}
.action{top:487px;height:28px;color:#fff;font-size:11px;text-align:center;line-height:28px}
.save{left:14px;width:105px;background:var(--salmon)}
.pay{left:134px;width:105px;background:var(--red)}
.chat{left:1072px;top:661px;width:37px;height:30px;background:var(--coral);display:flex;align-items:center;justify-content:center}

.footer{left:0;top:704px;width:1200px;height:39px;background:var(--white)}
.copyright{left:91px;top:718px;display:flex;align-items:center;gap:8px;font-size:11px;color:var(--muted)}
.store-badge{left:1024px;top:715px;width:85px;height:22px;background:#2b2b2b;border-radius:3px}
</style>
</head>
<body>
<div class="abs topbar">
  <div class="abs account-links"><span>Account: <b>20481937562</b></span><span>Support</span><span>Help</span><span>Feedback</span></div>
  <div class="abs user"><div class="avatar"></div>Hi, Sam Rivera
    <svg width="10" height="6" viewBox="0 0 10 6"><path d="M1 1l4 4 4-4" stroke="#777" fill="none"/></svg></div>
  <div class="abs register-tag">My Shop/Cash Register 1</div>
</div>

<div class="abs header"></div>
<div class="abs brand"><span class="brand-dot"></span>TillNest</div>
<div class="abs nav-btn active" style="left:301px;width:100px"><span class="nav-ico"></span>Enter Sale</div>
<div class="abs nav-btn" style="left:417px;width:178px"><span class="nav-ico"></span>Parked/Layby Orders<span class="badge">7</span></div>
<div class="abs nav-btn" style="left:609px;width:152px"><span class="nav-ico"></span>Completed Sales<span class="badge">3</span></div>
<div class="abs nav-btn" style="left:777px;width:140px"><span class="nav-ico"></span>Appointments<span class="badge">5</span></div>
<div class="abs nav-btn" style="left:936px;width:124px">
  <svg width="11" height="11" viewBox="0 0 11 11"><circle cx="4.5" cy="4.5" r="3.3" stroke="#fff" stroke-width="1.4" fill="none"/><path d="M7 7l3 3" stroke="#fff" stroke-width="1.5"/></svg>Back Office<span class="badge">2</span></div>
<div class="abs refresh"><svg width="14" height="14" viewBox="0 0 14 14"><path d="M11.5 5A5 5 0 0 0 2.5 5M2.5 9a5 5 0 0 0 9 0" stroke="#fff" stroke-width="1.4" fill="none"/><path d="M11.8 2v3.3H8.5M2.2 12V8.7h3.3" stroke="#fff" stroke-width="1.4" fill="none"/></svg></div>

<section class="abs panel products">
  <div class="panel-head"><span class="mini-mark"></span>Products Stats</div>
</section>
<div class="abs tile" style="left:107px;top:167px"><span class="initials">DP</span><span class="label">Demo Product</span></div>
<div class="abs tile" style="left:229px;top:167px"><span class="initials">EL</span><span class="label">Entry Level Co...</span></div>
<div class="abs tile" style="left:350px;top:167px"><span class="initials">GC</span><span class="label">Gift Cards</span></div>
<div class="abs tile" style="left:472px;top:167px"><span class="initials">P5</span><span class="label">Product 5</span></div>
<div class="abs tile" style="left:592px;top:167px"><span class="initials">T2</span><span class="label">Test 2</span></div>
<div class="abs tile" style="left:713px;top:167px"><span class="initials">T3</span><span class="label">Test 3</span></div>
<div class="abs tile" style="left:107px;top:275px"><span class="initials">T3</span><span class="label">Test 3</span></div>
<div class="abs tile" style="left:229px;top:275px"><span class="initials">FA</span><span class="label">fasdfadfasdf</span></div>
<div class="abs tile" style="left:350px;top:275px"><span class="initials">P3</span><span class="label">Product 3</span></div>
<div class="abs tile" style="left:472px;top:275px"><span class="initials">T3</span><span class="label">Test 3</span></div>
<div class="abs tile" style="left:592px;top:275px"><span class="initials">DP</span><span class="label">Demo Product</span></div>
<div class="abs tile" style="left:713px;top:275px"><span class="initials">P3</span><span class="label">Product 3</span></div>
<div class="abs tile" style="left:229px;top:384px"><span class="initials">DP</span><span class="label">Demo Product</span></div>
<div class="abs tile" style="left:350px;top:384px"><span class="initials">EL</span><span class="label">Entry Level Co...</span></div>
<div class="abs tile" style="left:472px;top:384px"><span class="initials">GC</span><span class="label">Gift Cards</span></div>
<div class="abs tile" style="left:592px;top:384px"><span class="initials">P5</span><span class="label">Product 5</span></div>
<div class="abs pager" style="left:108px;width:69px">Previous</div>
<div class="abs pager" style="left:745px;width:68px">Next</div>

<nav class="abs categories">
  <span class="arrow"><svg width="7" height="10" viewBox="0 0 7 10"><path d="M6 1L2 5l4 4" stroke="#fff" stroke-width="1.5" fill="none"/></svg></span>
  <span>LIST ALL</span><span>DEALS</span><span>UNCATEGORIZED</span><span class="fill"></span>
  <span class="arrow end"><svg width="7" height="10" viewBox="0 0 7 10"><path d="M1 1l4 4-4 4" stroke="#fff" stroke-width="1.5" fill="none"/></svg></span>
</nav>

<aside class="abs panel customer">
  <div class="panel-head"><span style="display:flex;align-items:center;gap:8px">
    <svg class="person" viewBox="0 0 11 13"><circle cx="5.5" cy="3.3" r="3" fill="#ec1f27"/><path d="M0 13c0-4 2.5-6 5.5-6S11 9 11 13z" fill="#ec1f27"/></svg>Select Customer</span>
    <svg width="10" height="6" viewBox="0 0 10 6"><path d="M1 1l4 4 4-4" stroke="#ec1f27" stroke-width="1.5" fill="none"/></svg></div>
  <div class="abs transaction">Transaction: <b>#98565</b></div>
  <div class="abs add-notes">Add Notes</div>
  <div class="abs totals">
    <div><span>Subtotal</span><em>$0.00</em></div>
    <div><span>Tax</span><em>$0.00</em></div>
    <div><span>Discount</span><em>$0.00</em></div>
    <div><span>Total</span><em>$0.00</em></div>
    <div><span>Paid</span><em>$0.00</em></div>
  </div>
  <div class="abs action save">SAVE &amp; PERK</div>
  <div class="abs action pay">PAY NOW</div>
</aside>
<div class="abs chat"><svg width="16" height="14" viewBox="0 0 16 14"><ellipse cx="8" cy="6.5" rx="6.8" ry="5.3" stroke="#fff" stroke-width="1.3" fill="none"/><path d="M5 6.5h6" stroke="#fff" stroke-width="1.3"/></svg></div>

<footer class="abs footer"></footer>
<div class="abs copyright"><span class="mini-mark"></span>Copyright © 2016 tillnest.com</div>
<div class="abs store-badge" role="img" aria-label="App store download badge"></div>
</body>
</html>
```